Etiketten-Design für Weißwein
Zielgruppe
Wir betreiben einen Weingroßhandel, beliefern die Gastronomie mit Wein und haben einen Onlineshop unter kerstel-wein.de
Zielgruppe für diesen Wein: Gastronomie und Privatkunden, Altersgruppe: 25-40, Charakteristiken: jung, aufgeschlossen und lebenslustig.
Aufgabenstellung
Zum Produkt: Flaschenform Bordeauxflasche, Inhalt Weißwein feinherb und wertig von einem Top Weingut, als Sommerwein gedacht.
Das Etikett soll modern sein und auffallen. Unsere erste Idee war MIRAVELLO mit einem Spruch: Kein Ziel, kein Plan, aber fantastischen Wein. Wir freuen uns aber auch über neue Ideen.
u.U. könnten weitere Weine mit diesem Etikett mit leichten Anpassungen entstehen (z.B. ein Rotwein und ein Rose)

```html
<!DOCTYPE html>
<html lang="de">
<head>
<meta charset="utf-8">
<title>MIRAVELLO – Weinetikett feinherb</title>
<link rel="stylesheet" href="https://fonts.googleapis.com/css2?family=Playfair+Display:wght@700;900&family=Jost:wght@400&display=swap">
<style>
  :root {
    --paper: #ffffff;
    --ink: #000000;
    --frame: #8a8a8a;
    --canvas: #ffffff;
  }
  * { margin: 0; padding: 0; box-sizing: border-box; }
  html, body {
    width: 1200px;
    height: 1200px;
    overflow: hidden;
    background: var(--canvas);
  }
  .label {
    position: absolute;
    left: 195px;
    top: 60px;
    width: 810px;
    height: 1080px;
    background: var(--paper);
    border: 1px solid var(--frame);
    overflow: hidden;
  }
  .label__wordmark {
    position: absolute;
    left: 0;
    top: 0;
    width: 810px;
    height: 520px;
    display: block;
  }
  .label__wordmark text {
    font-family: "Playfair Display", "Didot", serif;
    font-weight: 700;
    fill: var(--ink);
  }
  .label__slogan {
    position: absolute;
    left: 0;
    right: 0;
    top: 572px;
    text-align: center;
    font-family: "Jost", "Avenir Next", sans-serif;
    font-weight: 400;
    font-size: 41px;
    line-height: 57px;
    letter-spacing: 0.08em;
    color: var(--ink);
    text-transform: uppercase;
  }
  .label__rule {
    position: absolute;
    left: 95px;
    width: 620px;
    top: 913px;
    height: 3px;
    background: var(--ink);
  }
  .label__style {
    position: absolute;
    left: 0;
    right: 0;
    top: 992px;
    text-align: center;
    font-family: "Jost", "Avenir Next", sans-serif;
    font-weight: 400;
    font-size: 28px;
    letter-spacing: 0.14em;
    color: var(--ink);
    text-transform: uppercase;
  }
</style>
</head>
<body>
  <main class="label">
    <svg class="label__wordmark" viewBox="0 0 810 520" aria-label="MIRAVELLO">
      <text x="-6" y="266" font-size="240" textLength="822" lengthAdjust="spacingAndGlyphs">MIRA</text>
      <text x="-6" y="485" font-size="240" textLength="822" lengthAdjust="spacingAndGlyphs">VELLO</text>
    </svg>
    <p class="label__slogan">Kein Ziel,<br>kein Plan, aber<br>fantastischen<br>Wein</p>
    <div class="label__rule"></div>
    <p class="label__style">Feinherb</p>
  </main>
</body>
</html>
```